Reskinning of an eSport related app

We're looking for a redesign of an esport related community app. It should look very sharp and modern like trending fitness apps. Logo and general CI is done and fixed. UI needs to be reworked. In detail: - Overall GUI and Look and Feel - Playercard, Friends List, Achievement List - Icons for Achievements - Status system (Actually done via special borders) - Torvu Logo and dragon head are fixed, it can not be changed Actual Designs attached and so styles and look and feel we like. What we dont like very much at our actual design: - Look and feel of the borders. They need to look better and more modern. It is a break of the style - The look needs to be fresh, like fitness with asiatic touch - Good achievement icons are needed. Personal tryout link of the actual version: (It will mainly be used on mobile.) Https: //zq7arena.plomb. site / quick gear / people / 3a2d71c0-5b1e-4e2f-9c3a-7d8e0f1b2c44

```html
<!DOCTYPE html>
<html lang="en">
<head>
<meta charset="utf-8">
<title>Torvu app screens</title>
<link href="https://fonts.googleapis.com/css2?family=Lato:wght@400;700;900&display=swap" rel="stylesheet">
<style>
  :root{
    --stage:#68a7c2;
    --night-1:#1d3352;
    --night-2:#15243d;
    --night-3:#101c33;
    --card:rgba(70,88,112,.45);
    --card-line:rgba(205,215,228,.55);
    --ink:#ffffff;
    --ink-soft:#e4e9f0;
    --accent:#4aa3d8;
    --gold:#c8923f;
    --gold-light:#f0c77a;
    --common:#c02ad6;
    --rare:#3ec46a;
    --epic:#e02a2a;
    --disc:#0a0a0c;
  }
  *{box-sizing:border-box;margin:0;padding:0}
  html,body{width:1200px;height:521px;overflow:hidden;background:var(--stage)}
  body{position:relative;font-family:"Lato",sans-serif;color:var(--ink)}
  h1,h2,h3,p{font-weight:400}

  .screen{
    position:absolute;width:294.5px;overflow:hidden;
    background:
      radial-gradient(ellipse 70% 35% at 65% 30%, rgba(90,120,160,.45), transparent 70%),
      radial-gradient(ellipse 60% 30% at 30% 60%, rgba(80,105,140,.35), transparent 70%),
      linear-gradient(180deg,var(--night-1) 0%,var(--night-2) 55%,var(--night-3) 100%);
  }
  .screen--catalog{left:129.4px;top:48.5px;height:424px}
  .screen--profile{left:452.8px;top:15.3px;height:491px}
  .screen--friends{left:776px;top:48.5px;height:424px}

  .brand{position:absolute;display:flex;align-items:center;gap:8px;font-weight:900;font-size:30px;letter-spacing:.5px;color:var(--ink)}
  .brand__mark{width:32px;height:32px;border-radius:50%;background:var(--ink-soft)}
  .screen--catalog .brand,.screen--friends .brand{left:0;right:0;top:20px;justify-content:center}
  .screen--profile .brand{left:12px;top:22px}

  .tabs{position:absolute;top:76px;left:8px;right:8px;display:flex;gap:4.5px}
  .tab{flex:1;height:21.5px;border:1px solid var(--card-line);background:rgba(28,48,80,.8);
    font-size:8.6px;font-weight:700;text-transform:uppercase;display:flex;align-items:center;justify-content:center;letter-spacing:.2px}

  .card{position:absolute;left:8px;width:278.5px;height:67px;background:var(--card);border:1px solid var(--card-line)}
  .card__icon{position:absolute;left:13px;top:6.5px;width:54px;height:54px;border-radius:50%}
  .card__text{position:absolute;left:81.6px;top:11px;right:8px}
  .card__title{font-size:12.3px;line-height:14px;text-transform:uppercase;font-weight:400}
  .card__body{font-size:9.2px;line-height:14.7px;color:var(--ink-soft);font-weight:400}

  .badge{background:var(--disc);border:2.5px solid var(--gold);display:flex;align-items:center;justify-content:center}
  .badge svg{width:30px;height:30px}
  .badge__art{width:30px;height:30px;border-radius:50%;background:radial-gradient(circle,#f2f2f2 0%,#bdbdbd 70%,transparent 72%)}

  .avatar{border:3px solid var(--gold);background:radial-gradient(circle at 50% 40%,#b9a493 0%,#6d5a4d 55%,#2a2522 100%)}
  .avatar--gold{border:4px solid var(--gold-light)}
  .avatar--ruby{border-color:#d8262c;background:radial-gradient(circle at 50% 40%,#e6e2e0 0%,#8c7f80 55%,#3a1418 100%)}
  .avatar--silver{border-color:#c9ccd2;background:radial-gradient(circle at 50% 40%,#e3c2a7 0%,#b06a3d 55%,#4a2a1c 100%)}

  .count{position:absolute;font-size:8px;font-weight:700;right:8px}

  .login{position:absolute;top:30px;right:7px;display:flex;align-items:center;gap:5px;font-size:8.5px;font-weight:700;color:var(--accent)}
  .login__icon{width:21px;height:21px;border-radius:50%;border:1.3px solid var(--ink);display:flex;align-items:center;justify-content:center}
  .player{position:absolute;left:65.6px;top:82.8px;width:221px;height:66px;background:rgba(20,34,62,.9);border:2px solid var(--gold)}
  .player__avatar{position:absolute;left:9px;top:76.6px;width:80px;height:80px;border-radius:50%;border:5px solid var(--gold);background:radial-gradient(circle at 50% 40%,#c7ad95 0%,#7b6250 55%,#2b2420 100%)}
  .player__text{position:absolute;left:56px;top:16px}
  .player__name{font-size:12.3px;line-height:14px}
  .player__rank{font-size:9.2px;line-height:15px}
  .add-mate{position:absolute;right:7px;top:170px;font-size:8.3px;font-weight:700;display:flex;align-items:center;gap:5px}
  .add-mate__icon{width:7.5px;height:7.5px;border-radius:50%;background:var(--ink);color:var(--night-2);font-size:7px;line-height:7.5px;text-align:center;font-weight:900}
  .section-title{position:absolute;font-size:11.7px;text-transform:uppercase;font-weight:400}
  .gear{position:absolute;left:8px;top:208.6px;width:278.5px;height:108px;background:var(--card);border:1px solid var(--card-line)}
  .gear__image{position:absolute;left:14px;top:6px;width:77px;height:92px;border-radius:18px 18px 6px 6px;background:linear-gradient(160deg,#3a3a3c,#151517)}
  .gear__text{position:absolute;left:132px;top:28px}
  .gear__name{font-size:12.3px;line-height:15px}
  .gear__desc{font-size:9.2px;line-height:17px}
  .gear__date{font-size:9.2px;line-height:17px;color:var(--accent)}
  .pager{position:absolute;top:332.6px;left:119px;display:flex;gap:6px}
  .pager i{width:6.7px;height:6.7px;border-radius:50%;background:var(--ink)}
  .pager i.is-active{background:var(--accent)}
  .trophy{position:absolute;top:396.8px;width:53px;height:53px;border-radius:50%;background:var(--disc);
    display:flex;align-items:center;justify-content:center;font-size:27px;font-weight:900}
  .trophy--common{left:36px;border:2.5px solid var(--common)}
  .trophy--rare{left:122px;border:2.5px solid var(--rare)}
  .trophy--epic{left:206px;border:2.5px solid var(--epic)}
  .trophy-label{position:absolute;top:462px;width:53px;text-align:center;font-size:8.5px;font-weight:700}
</style>
</head>
<body>

<section class="screen screen--catalog">
  <div class="brand"><span class="brand__mark"></span>Torvu</div>
  <nav class="tabs">
    <span class="tab">Common</span><span class="tab">Rare</span><span class="tab">Epic</span><span class="tab">Upcoming</span>
  </nav>

  <article class="card" style="top:110.4px">
    <div class="card__icon badge"><div class="badge__art" role="img" aria-label="Wolf achievement emblem"></div></div>
    <div class="card__text"><h3 class="card__title">Wolf</h3><p class="card__body">Lorem ipsum dolor sit amet, consectetur adipiscing elit.</p></div>
  </article>
  <article class="card" style="top:183.4px">
    <div class="card__icon badge">
      <svg viewBox="0 0 30 30" fill="none" stroke="#fff" stroke-width="1.6"><rect x="5" y="6" width="20" height="18"/><path d="M11 6v18M19 6v18"/><path d="M8 11l2 2M10 11l-2 2M14 17l3-3 4 3" stroke-width="1.2"/></svg>
    </div>
    <div class="card__text"><h3 class="card__title">Karte</h3><p class="card__body">Lorem ipsum dolor sit amet, consectetur adipiscing elit.</p></div>
  </article>
  <article class="card" style="top:257px">
    <div class="card__icon badge">
      <svg viewBox="0 0 30 30" fill="none" stroke="#fff" stroke-width="2.4" stroke-linecap="round"><path d="M6 6l18 18M24 6L6 24"/><path d="M4 21l5 5M26 21l-5 5" stroke-width="2"/></svg>
    </div>
    <div class="card__text"><h3 class="card__title">Kampf</h3><p class="card__body">Lorem ipsum dolor sit amet, consectetur adipiscing elit.</p></div>
  </article>
  <article class="card" style="top:330px">
    <div class="card__icon badge">
      <svg viewBox="0 0 30 30" fill="none" stroke="#fff" stroke-width="1.3"><path d="M15 3c4 4 5 9 3 15h-6c-2-6-1-11 3-15z"/><circle cx="15" cy="11" r="2"/><path d="M12 18l-3 3h3M18 18l3 3h-3M13 21l2 3 2-3"/><path d="M4 26c2-2 4-2 6 0 2-2 4-2 6 0 2-2 4-2 6 0 2-2 3-1 4 0"/></svg>
    </div>
    <div class="card__text"><h3 class="card__title">Rakete</h3><p class="card__body">Lorem ipsum dolor sit amet, consectetur adipiscing elit.</p></div>
  </article>
  <span class="count" style="top:408px">X10</span>
</section>

<section class="screen screen--profile">
  <div class="brand"><span class="brand__mark"></span>Torvu</div>
  <div class="login">
    <span class="login__icon"><svg width="10" height="11" viewBox="0 0 10 11" fill="#fff"><circle cx="5" cy="3" r="2.6"/><path d="M0 11c0-3.5 2-5 5-5s5 1.5 5 5z"/></svg></span>
    LOG IN
  </div>
  <div class="player">
    <div class="player__text"><h2 class="player__name">MY FACE</h2><p class="player__rank">Warrior inTraining</p></div>
  </div>
  <div class="player__avatar" role="img" aria-label="Player portrait in a gold status border"></div>
  <div class="add-mate"><span class="add-mate__icon">+</span>ADD MATE</div>

  <h2 class="section-title" style="left:8px;top:191px">Equipment</h2>
  <article class="gear">
    <div class="gear__image" role="img" aria-label="Black hooded sweatshirt"></div>
    <div class="gear__text">
      <h3 class="gear__name">THE WOLF</h3>
      <p class="gear__desc">Nulla vitae ante metus</p>
      <p class="gear__date">Equipped: 26 March 2019</p>
    </div>
  </article>
  <div class="pager"><i class="is-active"></i><i></i><i></i><i></i><i></i></div>

  <h2 class="section-title" style="left:0;right:0;text-align:center;top:368px">Achievements</h2>
  <div class="trophy trophy--common">5</div>
  <div class="trophy trophy--rare">5</div>
  <div class="trophy trophy--epic">5</div>
  <span class="trophy-label" style="left:36px;color:var(--common)">COMMON</span>
  <span class="trophy-label" style="left:122px;color:var(--rare)">RARE</span>
  <span class="trophy-label" style="left:206px;color:var(--epic)">EPIC</span>
  <span class="count" style="top:476px">X10</span>
</section>

<section class="screen screen--friends">
  <div class="brand"><span class="brand__mark"></span>Torvu</div>

  <article class="card" style="top:79.8px">
    <div class="card__icon avatar" role="img" aria-label="Friend portrait with bronze border"></div>
    <div class="card__text"><h3 class="card__title">My Face</h3><p class="card__body">Worrior in Training<br>Status: Bronze</p></div>
  </article>
  <article class="card" style="top:152.8px">
    <div class="card__icon avatar avatar--gold" role="img" aria-label="Friend portrait with gold border"></div>
    <div class="card__text"><h3 class="card__title">My Face</h3><p class="card__body">Worrior in Training<br>Status: Bronze</p></div>
  </article>
  <article class="card" style="top:226.4px">
    <div class="card__icon avatar avatar--ruby" role="img" aria-label="Friend portrait with red border"></div>
    <div class="card__text"><h3 class="card__title">My Face</h3><p class="card__body">Worrior in Training<br>Status: Bronze</p></div>
  </article>
  <article class="card" style="top:299.4px">
    <div class="card__icon avatar avatar--silver" role="img" aria-label="Friend portrait with silver border"></div>
    <div class="card__text"><h3 class="card__title">My Face</h3><p class="card__body">Worrior in Training<br>Status: Bronze</p></div>
  </article>
  <span class="count" style="top:408px">X10</span>
</section>

</body>
</html>
```